E brochure for company overview

We need a brochure for a company overview that will be sent to potential new clients. We are uploading a file with all the content that needs to be included inside of the brochure. We need this content to be displayed in a professional, neat, and creative way. The file has a Spanish and English version so we need two versions of the brochure in each language. *This brochure will be viewed digitally and it will not be printed, thus it does not need a cover page*. We included our company logo (Parvolux) Please utilize this in your design.

```html
<!DOCTYPE html>
<html lang="en">
<head>
<meta charset="utf-8">
<title>Parvolux – Company Overview</title>
<link href="https://fonts.googleapis.com/css2?family=Barlow:wght@400;500;600;700;800&display=swap" rel="stylesheet">
<style>
  :root {
    --paper: #f1f1f1;
    --ink: #1d1d1f;
    --red: #d32f34;
    --red-text: #d0252f;
    --black: #0c0c0c;
    --orange: #ee8f3a;
    --band: #dcdcdc;
    --grey-text: #4a4a4a;
    --white: #ffffff;
  }
  * { margin: 0; padding: 0; box-sizing: border-box; }
  html, body { width: 1135px; height: 1200px; overflow: hidden; }
  body { background: var(--paper); font-family: "Barlow", Arial, sans-serif; color: var(--ink); }
  .brochure { position: relative; width: 1135px; height: 1200px; background: var(--paper); overflow: hidden; }

  .accent-block { position: absolute; left: 758px; top: 0; width: 377px; height: 403px; background: var(--black); }
  .hero-photo { position: absolute; left: 506px; top: 30px; width: 593px; height: 628px;
    background: linear-gradient(160deg, #b9d3cf 0%, #8fb0ad 35%, #6d7f78 60%, #c9d5d2 78%, #3d4a4c 100%); }

  .brand { position: absolute; left: 65px; top: 62px; display: flex; align-items: center; gap: 14px; }
  .brand-mark { width: 64px; height: 64px; border-radius: 50%; background: var(--red); }
  .brand-name { font-size: 50px; font-weight: 700; color: var(--ink); line-height: 1; letter-spacing: 0.5px; }
  .brand-tagline { font-size: 19px; font-weight: 600; color: var(--ink); margin-top: 4px; letter-spacing: 0.4px; }

  .about { position: absolute; left: 65px; width: 375px; }
  .about h2 { font-size: 22px; font-weight: 700; letter-spacing: 4px; color: var(--red-text); margin-bottom: 4px; line-height: 1.2; }
  .about p { font-size: 16px; line-height: 18px; color: var(--ink); }
  .about.history { top: 167px; }
  .about.mission { top: 292px; }
  .about.vision { top: 418px; }
  .website { position: absolute; left: 65px; top: 562px; font-size: 22px; font-weight: 700; letter-spacing: 4.5px; color: var(--grey-text); }

  .services { position: absolute; left: 40px; top: 600px; width: 539px; height: 600px; background: var(--red); color: var(--white); }
  .services h2 { position: absolute; left: 37px; top: 32px; font-size: 70px; line-height: 0.93; font-weight: 700; letter-spacing: 2px; }
  .service { position: absolute; display: flex; align-items: center; gap: 14px; font-size: 19px; font-weight: 500; letter-spacing: 1px; line-height: 1.15; text-transform: uppercase; }
  .service svg { width: 54px; height: 54px; flex: none; }
  .service.s1 { left: 30px; top: 190px; }
  .service.s2 { left: 285px; top: 190px; }
  .service.s3 { left: 30px; top: 292px; }
  .service.s4 { left: 285px; top: 292px; }
  .service.s5 { left: 30px; top: 402px; }
  .service.s6 { left: 285px; top: 402px; }

  .values { position: absolute; left: 628px; top: 690px; }
  .values h2 { font-size: 40px; font-weight: 700; letter-spacing: 3px; color: var(--red-text); margin-bottom: 22px; }
  .values ul { list-style: none; }
  .values li { display: flex; align-items: center; gap: 22px; height: 63px; font-size: 30px; font-weight: 700; letter-spacing: 3px; color: var(--ink); }
  .values li svg { width: 44px; height: 44px; flex: none; }

  .partners-band { position: absolute; left: 40px; top: 1094px; width: 644px; height: 70px; background: var(--band);
    display: flex; align-items: center; justify-content: space-around; padding: 0 14px; }
  .partner { font-size: 30px; font-weight: 700; color: #3b3b3b; letter-spacing: 0.3px; }
  .partners-title { position: absolute; left: 684px; top: 1094px; width: 451px; height: 70px; background: var(--orange);
    display: flex; align-items: center; justify-content: center; font-size: 38px; font-weight: 700; letter-spacing: 3.5px; color: #fbe9d9; }
</style>
</head>
<body>
<main class="brochure">
  <div class="accent-block"></div>
  <div class="hero-photo" role="img" aria-label="Photo of a consultant's hands taking notes beside open laptops on a desk"></div>

  <header class="brand">
    <span class="brand-mark"></span>
    <div>
      <div class="brand-name">PARVOLUX</div>
      <div class="brand-tagline">IT CONSULTING AND SERVICES</div>
    </div>
  </header>

  <section class="about history">
    <h2>HISTORY</h2>
    <p>Parvolux initiates on 2006 Parvolux has 15 years in the technology industry, specialising in security management, infrastructure and service management.</p>
  </section>
  <section class="about mission">
    <h2>MISSION</h2>
    <p>Providing our customers with the best human and technological resources with the clear objective of providing effective solutions using best industry practices .</p>
  </section>
  <section class="about vision">
    <h2>VISION</h2>
    <p>To be recognized by our customers ascan important company in the Dominican Republic in the area of security and infrastructure and achieve presence throughout the Caribbean and Central America.</p>
  </section>
  <div class="website">WWW.PARVOLUX.COM</div>

  <section class="services">
    <h2>OUR<br>SERVICES</h2>
    <div class="service s1">
      <svg viewBox="0 0 48 48" fill="none" stroke="#fff" stroke-width="3.5" stroke-linecap="round"><circle cx="12" cy="15" r="4"/><line x1="24" y1="15" x2="38" y2="15"/><line x1="8" y1="33" x2="22" y2="33"/><circle cx="34" cy="33" r="4"/></svg>
      <span>Service<br>Management</span>
    </div>
    <div class="service s2">
      <svg viewBox="0 0 48 48" fill="none" stroke="#fff" stroke-width="3.5" stroke-linejoin="round" stroke-linecap="round"><path d="M24 5 L40 11 V24 C40 34 32 40 24 43 C16 40 8 34 8 24 V11 Z"/><path d="M17 24 L22 29 L31 19"/></svg>
      <span>Security of<br>Information</span>
    </div>
    <div class="service s3">
      <svg viewBox="0 0 48 48" fill="none" stroke="#fff" stroke-width="3.5" stroke-linejoin="round" stroke-linecap="round"><rect x="6" y="8" width="34" height="34" rx="8"/><path d="M20 30 L21 23 L36 8 L42 14 L27 29 Z"/></svg>
      <span>Custom<br>Development</span>
    </div>
    <div class="service s4">
      <svg viewBox="0 0 48 48" fill="none" stroke="#fff" stroke-width="3.5" stroke-linecap="round"><circle cx="21" cy="21" r="15"/><line x1="32" y1="32" x2="42" y2="42"/></svg>
      <span>Device and<br>Network<br>Monitoring</span>
    </div>
    <div class="service s5">
      <svg viewBox="0 0 48 48" fill="none" stroke="#fff" stroke-width="3.5" stroke-linejoin="round" stroke-linecap="round"><rect x="6" y="6" width="36" height="36" rx="9"/><path d="M16 24 L22 30 L32 18"/></svg>
      <span>DevOps</span>
    </div>
    <div class="service s6">
      <svg viewBox="0 0 48 48" fill="none" stroke="#fff" stroke-width="3.5" stroke-linejoin="round" stroke-linecap="round"><path d="M6 14 C6 10 8 8 12 8 H19 L23 12 H36 C40 12 42 14 42 18 V36 C42 40 40 42 36 42 H12 C8 42 6 40 6 36 Z"/><line x1="6" y1="22" x2="42" y2="22"/></svg>
      <span>API<br>Management</span>
    </div>
  </section>

  <section class="values">
    <h2>STAFFING VALUES</h2>
    <ul>
      <li><svg viewBox="0 0 48 48" fill="none" stroke="#d0252f" stroke-width="3" stroke-linejoin="round"><path d="M24 5 L29.5 17 L42 18.5 L32.5 27 L35.5 40 L24 33 L12.5 40 L15.5 27 L6 18.5 L18.5 17 Z"/></svg>INTEGRITY</li>
      <li><svg viewBox="0 0 48 48" fill="none" stroke="#d0252f" stroke-width="3" stroke-linejoin="round" stroke-linecap="round"><path d="M8 40 L10 30 L30 8 L38 16 L18 38 Z"/><line x1="24" y1="42" x2="40" y2="42"/></svg>CREATIVITY</li>
      <li><svg viewBox="0 0 48 48" fill="none" stroke="#d0252f" stroke-width="3" stroke-linecap="round"><circle cx="18" cy="15" r="7"/><path d="M5 38 C5 30 11 26 18 26 C25 26 31 30 31 38"/><path d="M30 8 C35 9 37 13 36 17 C35 20 33 22 30 22"/><path d="M36 27 C40 29 43 33 43 38"/></svg>TEAM WORK</li>
      <li><svg viewBox="0 0 48 48" fill="none" stroke="#d0252f" stroke-width="3" stroke-linejoin="round" stroke-linecap="round"><rect x="7" y="7" width="34" height="34" rx="9"/><path d="M16 24 L22 30 L32 18"/></svg>POSITIVE ATTITUDE</li>
      <li><svg viewBox="0 0 48 48" fill="none" stroke="#d0252f" stroke-width="3" stroke-linejoin="round" stroke-linecap="round"><path d="M15 20 V14 C15 9 19 5 24 5 C29 5 33 9 33 14 V20"/><rect x="9" y="20" width="30" height="23" rx="6"/><line x1="24" y1="28" x2="24" y2="34"/></svg>COMMITMENT</li>
    </ul>
  </section>

  <div class="partners-band">
    <span class="partner">Halvex</span>
    <span class="partner">Nordwave</span>
    <span class="partner">Quorvane</span>
    <span class="partner">Kevanto</span>
  </div>
  <div class="partners-title">OUR PARTNERS</div>
</main>
</body>
</html>
```